Verdon Ridgeworks Ltd. - Refreshed business card challenge

A revised, refreshed business card design for my oil and gas company using my existing logo. Feel free to be as creative as you like!

Target Market(s)

bankers, lawyers

Industry/Entity Type

Oil And Gas Exploration

Contact Information for Business Card

See the "Must Haves" section

Font styles to use
Serif
Sans Serif

Colors

Designer to choose colors to be used in the design.

Requirements
Must have
• Existing business logo, name, title, email, phone number, business address
• Neil Hastow, CA, CPA
• Vice President Finance & Chief Financial Officer
• nhastow@verdonridgeworks.example
• office: (555)284-6071
• cell: (555)716-3342
• 840, 615 11 Street N.E.
• Calgary, AB
• X9Q 4K1
Should not have
• Should not be plain and boring.

```html
<!DOCTYPE html>
<html lang="en">
<head>
<meta charset="utf-8">
<title>Verdon Ridgeworks Ltd. – Business Card</title>
<link rel="stylesheet" href="https://fonts.googleapis.com/css2?family=Archivo:wght@800&family=Oswald:wght@500&family=Roboto:wght@400&display=swap">
<style>
  :root {
    --backdrop: #bfbfbf;
    --forest: #0d4a32;
    --forest-deep: #0b3d29;
    --bark: #4a2410;
    --bark-deep: #3d1c0b;
    --paper: #f4f4f2;
    --ink-light: #ffffff;
    --ink-soft: #e6ece8;
  }
  * { margin: 0; padding: 0; box-sizing: border-box; }
  html, body {
    width: 1200px; height: 576px; overflow: hidden;
    background: var(--backdrop);
  }
  .stage { position: relative; width: 1200px; height: 576px; }

  .card {
    position: absolute; top: 140px;
    width: 482px; height: 294px;
    border-radius: 14px; overflow: hidden;
    box-shadow: 0 3px 6px rgba(0,0,0,0.25);
  }

  /* Front */
  .card--front {
    left: 82px;
    background: linear-gradient(115deg, var(--bark) 0%, #1e3a22 40%, var(--forest) 100%);
    display: flex; align-items: center; justify-content: center;
  }
  .front-wordmark {
    font-family: "Archivo", "Arial Black", sans-serif;
    font-weight: 800; font-size: 40px; letter-spacing: -0.5px;
    color: var(--ink-soft);
  }

  /* Back */
  .card--back { left: 602px; }
  .back-shapes { position: absolute; inset: 0; width: 482px; height: 294px; }

  .back-wordmark {
    position: absolute; right: 26px; top: 120px;
    font-family: "Archivo", "Arial Black", sans-serif;
    font-weight: 800; font-size: 22px; letter-spacing: -0.3px;
    color: var(--forest);
  }

  .holder { position: absolute; left: 22px; top: 50px; color: var(--ink-light); }
  .holder-name {
    font-family: "Oswald", "Arial Narrow", sans-serif;
    font-weight: 500; font-size: 18px; line-height: 1.2;
  }
  .holder-title {
    margin-top: 6px;
    font-family: "Roboto", Arial, sans-serif;
    font-size: 11.5px; line-height: 15px; color: var(--ink-soft);
  }

  .contact-list {
    position: absolute; left: 22px; top: 184px;
    list-style: none;
    font-family: "Roboto", Arial, sans-serif;
    font-size: 12px; line-height: 16.3px; color: var(--ink-soft);
  }
  .contact-list li { display: flex; align-items: center; gap: 8px; }
  .contact-icon { width: 10px; height: 10px; flex: none; fill: var(--ink-soft); }

  .address {
    position: absolute; left: 22px; top: 256px;
    font-family: "Roboto", Arial, sans-serif;
    font-size: 12px; color: var(--ink-soft);
  }
</style>
</head>
<body>
<main class="stage">

  <section class="card card--front" aria-label="Business card front">
    <span class="front-wordmark">Verdon Ridgeworks</span>
  </section>

  <section class="card card--back" aria-label="Business card back">
    <svg class="back-shapes" viewBox="0 0 482 294" aria-hidden="true">
      <defs>
        <linearGradient id="back-base" x1="0" y1="0" x2="1" y2="1">
          <stop offset="0" stop-color="#0c4630"/>
          <stop offset="0.55" stop-color="#123a24"/>
          <stop offset="0.8" stop-color="#3a2210"/>
          <stop offset="1" stop-color="#4a2410"/>
        </linearGradient>
      </defs>
      <rect width="482" height="294" fill="url(#back-base)"/>
      <path d="M148,0 C200,0 205,70 235,120 C265,166 322,190 402,192 L482,192 V0 Z" fill="#3d1c0b"/>
      <path d="M148,0 C200,0 205,70 235,120 C265,166 322,188 402,189 L482,189 V0 Z" fill="#0d4a32"/>
      <path d="M152,0 C202,0 207,68 237,116 C267,161 322,183 402,184 L482,184 V0 Z" fill="#f4f4f2"/>
    </svg>

    <span class="back-wordmark">Verdon Ridgeworks</span>

    <div class="holder">
      <h1 class="holder-name">Neil Hastow, CA, CPA</h1>
      <p class="holder-title">Vice President Finance &amp;<br>Chief Financial Officer</p>
    </div>

    <ul class="contact-list">
      <li>
        <svg class="contact-icon" viewBox="0 0 10 10" aria-hidden="true"><path d="M1,3 Q5,0 9,3 L8,4.5 L6.5,3.8 L6.5,3 Q5,2.5 3.5,3 L3.5,3.8 L2,4.5 Z M2.5,5 H7.5 L8.5,9 H1.5 Z"/></svg>
        (555) 284-6071
      </li>
      <li>
        <svg class="contact-icon" viewBox="0 0 10 10" aria-hidden="true"><path d="M2.5,0.5 H7.5 V3 H2.5 Z M0.5,3.5 H9.5 V7.5 H8 V6 H2 V7.5 H0.5 Z M2.5,6.5 H7.5 V9.5 H2.5 Z"/></svg>
        (555) 716-3342
      </li>
      <li>
        <svg class="contact-icon" viewBox="0 0 10 10" aria-hidden="true"><path d="M0.5,2 H9.5 V8.5 H0.5 Z" fill="none" stroke="#e6ece8"/><path d="M0.5,2 L5,6 L9.5,2" fill="none" stroke="#e6ece8"/></svg>
        nhastow@verdonridgeworks.example
      </li>
      <li>
        <svg class="contact-icon" viewBox="0 0 10 10" aria-hidden="true"><circle cx="5" cy="5" r="4.3" fill="none" stroke="#e6ece8"/><ellipse cx="5" cy="5" rx="1.8" ry="4.3" fill="none" stroke="#e6ece8" stroke-width="0.8"/><path d="M0.7,5 H9.3" stroke="#e6ece8" stroke-width="0.8"/></svg>
        www.verdonridgeworks.example
      </li>
    </ul>

    <p class="address">840, 615 11 Street N.E. Calgary, AB X9Q 4K1</p>
  </section>

</main>
</body>
</html>
```